business card design

i would like business cards designed. My business provides trade qualified personnel to the mining industry to work on heavy mobile equipment.
please put a excavator(digger) in the background in one design and have one design without so i can compare the difference.
also add info:
my logo(attached) and "mobile equipment repair and maintenance"
name: Derek Holloway
address: 57 Tarrowby RD Wendale Perth WA.
mobile: 0438120957
email: derek@ironvalemx.com

```html
<!DOCTYPE html>
<html lang="en">
<head>
<meta charset="utf-8">
<title>Ironvale Maintenance Services – Business Cards</title>
<link href="https://fonts.googleapis.com/css2?family=Montserrat:wght@500;600;800&family=Oswald:wght@600&display=swap" rel="stylesheet">
<style>
  :root {
    --navy: #0c1f45;
    --navy-deep: #091836;
    --accent: #4a7bd0;
    --white: #ffffff;
    --soft-white: #dfe6f2;
    --backdrop: #333333;
  }
  * { margin: 0; padding: 0; box-sizing: border-box; }
  html, body {
    width: 1200px; height: 900px; overflow: hidden;
    background: var(--backdrop);
    font-family: "Montserrat", sans-serif;
  }
  .sheet {
    width: 1200px; height: 900px;
    display: flex; flex-direction: column;
    align-items: center; justify-content: center; gap: 40px;
  }
  .card {
    width: 640px; height: 366px;
    position: relative; overflow: hidden;
    box-shadow: 0 14px 30px rgba(0,0,0,.45);
  }

  /* Front */
  .card--front { background: var(--navy); }
  .front-top {
    position: absolute; left: 0; top: 0; width: 100%; height: 196px;
    background: var(--white);
    border-bottom: 5px solid var(--accent);
    display: flex; flex-direction: column; align-items: center; justify-content: center;
  }
  .brand-name {
    font-weight: 800; letter-spacing: 2px; line-height: 1;
    display: flex; align-items: center; gap: 12px;
  }
  .brand-name .mark { width: 14px; height: 14px; background: var(--accent); }
  .front-top .brand-name { font-size: 64px; color: var(--navy); }
  .brand-sub {
    font-weight: 600; font-size: 13px; letter-spacing: 2.4px;
    color: var(--accent); margin-top: 10px;
  }
  .front-bottom {
    position: absolute; left: 0; top: 201px; width: 100%; height: 165px;
    display: flex; align-items: center; justify-content: center; padding: 0 30px;
  }
  .person { text-align: right; padding-right: 26px; white-space: nowrap; }
  .person-name {
    font-family: "Oswald", sans-serif; font-weight: 600;
    font-size: 32px; letter-spacing: 1px; color: var(--accent);
    text-transform: uppercase; line-height: 1.1;
  }
  .person-role { font-size: 15px; color: var(--white); margin-top: 6px; font-weight: 500; }
  .divider { width: 1px; height: 96px; background: var(--accent); flex: none; }
  .contact { padding-left: 26px; color: var(--white); font-size: 15px; line-height: 1.45; font-weight: 500; white-space: nowrap; }
  .contact-line { display: flex; align-items: center; gap: 8px; }
  .contact-line svg { width: 12px; height: 12px; flex: none; }
  .contact-line .icon-space { width: 12px; flex: none; }

  /* Back */
  .card--back {
    background: var(--navy-deep);
    display: flex; flex-direction: column; align-items: center; justify-content: center;
  }
  .card--back .brand-name { font-size: 68px; color: var(--white); }
  .card--back .brand-sub { font-size: 14px; }
  .tagline {
    font-weight: 600; font-size: 12px; letter-spacing: 2.2px;
    color: var(--soft-white); margin-top: 6px; text-transform: uppercase;
  }
</style>
</head>
<body>
<main class="sheet">
  <section class="card card--front" aria-label="Business card front">
    <div class="front-top">
      <div class="brand-name"><span class="mark"></span>IRONVALE</div>
      <div class="brand-sub">MAINTENANCE SERVICES PTY LTD</div>
    </div>
    <div class="front-bottom">
      <div class="person">
        <div class="person-name">Derek Holloway</div>
        <div class="person-role">Director</div>
      </div>
      <div class="divider"></div>
      <div class="contact">
        <div class="contact-line"><span class="icon-space"></span>57 Tarrowby RD</div>
        <div class="contact-line"><span class="icon-space"></span>Wendale Perth WA.</div>
        <div class="contact-line">
          <svg viewBox="0 0 12 12" aria-hidden="true"><path d="M3 1 L5 3.5 L4 5 Q5 7 7 8 L8.5 7 L11 9 L9.5 11 Q4 10.5 1 3 Z" fill="var(--accent)"/></svg>
          0438120957
        </div>
        <div class="contact-line">
          <svg viewBox="0 0 12 12" aria-hidden="true"><rect x="1" y="2.5" width="10" height="7" fill="none" stroke="var(--accent)" stroke-width="1.3"/><path d="M1 3 L6 6.8 L11 3" fill="none" stroke="var(--accent)" stroke-width="1.3"/></svg>
          derek@ironvalemx.com
        </div>
      </div>
    </div>
  </section>

  <section class="card card--back" aria-label="Business card back">
    <div class="brand-name"><span class="mark"></span>IRONVALE</div>
    <div class="brand-sub">MAINTENANCE SERVICES PTY LTD</div>
    <div class="tagline">Mobile equipment repair and maintenance</div>
  </section>
</main>
</body>
</html>
```